Web Design Project

The Varnholt Group is a strategy consulting group that works primarily with the healthcare industry. We provide a limited range of strategic planning & marketing services designed to focus on the growth and future viability of our clients’ organizations. We are a very small organization, but want to communicate a sense of boldness, forward-looking/visionary, and both creative and analytic. What follows below is: 1) A simple overview of the outline of the web-pages; 2) an important list of web-sites that appeal to me – the most important of which appears in a larger font; 3) photo ideas for the home page (from Pictavo.com). I have not written copy…and won’t until I know length based upon design.

The Varnholt Group
Healthcare Strategic Consulting

(Key Sections for the site)
HOME PAGE ABOUT US SERVICES NEWS & COMMENTS CONTACT US

(Sites That I Admire:)

http://www.lumenwirk.eu/services/ Very creative use of iconography to represent services, etc.

http://quillmoss.com/ Arresting graphics

http://brontiva.co/ GREAT SITE. THIS IS THE SITE THAT I LIKE THE MOST IN TERMS OF GENERAL LOOK & FEEL.

http://kasperholm.com/ Very interesting, stark/bold B&W site for architects

http://www.rtmalvey.com/ Interesting home page for promoting individual

HOME PAGE:

The Varnholt Group
STRATEGIC CONSULTING SERVICES (should be bold). We have a Logo that can be supplied later

Pictavo Image Options: 47193652, 36840157, 29617483, 58302619, 274815936, 61948237
Updates

Project Deadline Extended
Reason: The 1st and 2nd place designers will have an additional 5-7 days to complete the remaining pages of the site (approximately 11 pages). I have a file with all the photo information and rough copy that can be dropped into position.

Target Market(s)

Senior Executives (CEO,COO, CFO,SVP) in major hospitals or healthcare systems, other senior executives within healthcare.

Industry/Entity Type

Healthcare

Requirements
Must have
• I will want to pay to have this project expanded to show look and feel for:
*Home Page and key sections
*4 Pages that will be under the "About Us" heading
*5 Pages that will be under the "Services" heading

I have image options selected from Pictavo for all key sections. We will need to look at the cost for those images that the designer recommends.

```html
<!DOCTYPE html>
<html lang="en">
<head>
<meta charset="utf-8">
<title>The Varnholt Group – Healthcare Strategic Consulting</title>
<link rel="stylesheet" href="https://fonts.googleapis.com/css2?family=PT+Sans:wght@400;700&family=PT+Sans+Narrow:wght@700&display=swap">
<style>
:root{
  --navy:#0b1f7a;
  --navy-deep:#071660;
  --sky-top:#1d63d8;
  --sky-mid:#4b9be6;
  --sky-low:#a9d3f3;
  --ink:#2b2b2b;
  --ink-soft:#4a4a4a;
  --slate:#34495e;
  --news-body:#55606c;
  --charcoal:#363636;
  --white:#ffffff;
  --panel:#f2f2f2;
  --rule:#cfcfcf;
  --button-dark:#2a2a2a;
}
*{box-sizing:border-box;margin:0;padding:0}
html,body{width:1200px;height:2233px;overflow:hidden}
body{font-family:"PT Sans",Arial,sans-serif;color:var(--ink);background:var(--white);position:relative}
.condensed{font-family:"PT Sans Narrow","Arial Narrow",sans-serif;font-weight:700}

/* header */
.site-header{position:absolute;left:0;top:0;width:1200px;height:118px;z-index:2;
  background:linear-gradient(90deg,var(--navy-deep) 0%,var(--navy) 55%,rgba(40,80,170,.85) 100%);}
.brand{position:absolute;left:58px;top:34px;color:var(--white)}
.brand-name{font-family:"PT Sans",sans-serif;font-weight:700;font-size:30px;letter-spacing:-.3px;line-height:1}
.brand-tag{font-size:13px;font-weight:700;margin-top:8px;padding-left:18px}
.main-nav{position:absolute;right:52px;top:62px;display:flex;align-items:center;color:var(--white);font-size:16px}
.main-nav a{color:inherit;text-decoration:none;padding:0 21px;border-left:1px solid rgba(255,255,255,.55);line-height:16px}
.main-nav a:first-child{border-left:none}

/* hero */
.hero{position:absolute;left:0;top:0;width:1200px;height:670px;overflow:hidden}
.hero-photo{position:absolute;inset:0;background:linear-gradient(180deg,var(--sky-top) 0%,var(--sky-mid) 50%,var(--sky-low) 100%)}
.hero-copy{position:absolute;left:0;right:0;top:292px;text-align:center;color:var(--white)}
.hero-title{font-size:66px;line-height:1;letter-spacing:-.5px}
.hero-text{font-size:23px;line-height:26px;width:830px;margin:14px auto 0}
.hero-button{display:inline-block;margin-top:30px;background:#dff1fb;color:#16325c;font-size:16px;padding:7px 14px;border-radius:2px}
.hero-arrow{position:absolute;top:335px}
.hero-arrow.prev{left:38px}
.hero-arrow.next{right:38px}

/* welcome */
.welcome{position:absolute;left:0;top:670px;width:1200px;height:321px}
.welcome-main{position:absolute;left:57px;top:30px;width:677px}
.section-title{font-size:24px;color:var(--ink);letter-spacing:.2px;text-transform:uppercase}
.welcome-lead{font-weight:700;font-size:14px;line-height:22px;margin-top:14px}
.welcome-body{font-size:14px;line-height:22px;color:var(--ink-soft);margin-top:12px}
.more-link{display:inline-flex;align-items:center;gap:5px;font-size:14px;margin-top:14px;color:var(--ink);text-transform:uppercase}
.video-block{position:absolute;left:798px;top:30px}
.video-frame{width:336px;height:228px;background:#000;margin-top:14px;display:flex;align-items:center;justify-content:center}

/* featured */
.featured{position:absolute;left:0;top:991px;width:1200px;height:404px;background:var(--charcoal);color:var(--white)}
.featured .section-title{color:var(--white);position:absolute;left:57px;top:30px}
.service{position:absolute;top:75px;width:340px}
.service-frame{width:331px;height:178px;background:var(--white);padding:9px}
.service-photo{width:100%;height:100%}
.service h3{font-size:15px;font-weight:700;margin:19px 0 0 2px;text-transform:uppercase}
.service p{font-size:14px;line-height:22px;margin:6px 0 0 2px}

/* news */
.news{position:absolute;left:0;top:1395px;width:1200px;height:497px}
.news .section-title{position:absolute;left:54px;top:38px;color:var(--slate)}
.news-item{position:absolute;width:340px}
.news-item h4{font-size:13px;line-height:21px;font-weight:700;color:var(--slate);text-transform:uppercase;letter-spacing:.2px;padding-right:40px}
.news-item p{font-size:12.5px;line-height:21px;color:var(--news-body);margin-top:3px}
.news-item .more-link{font-size:12px;margin-top:6px;color:var(--slate)}
.news-divider{position:absolute;left:51px;top:258px;width:1097px;border-top:1px dashed #9a9a9a}

/* footer */
.site-footer{position:absolute;left:0;top:1892px;width:1200px;height:341px;background:var(--panel)}
.footer-col{position:absolute;top:48px}
.footer-col h5{font-size:17px;font-weight:400;color:var(--ink);letter-spacing:.4px;text-transform:uppercase}
.footer-col p{font-size:12.5px;line-height:20px;color:var(--ink-soft);margin-top:6px}
.footer-sep{position:absolute;top:40px;width:1px;height:190px;background:var(--rule)}
.social{display:flex;gap:26px;margin-top:20px;padding-left:6px}
.social span{width:22px;height:22px;border-radius:50%;background:#4a4a4a}
.newsletter-input{width:292px;height:34px;border:1px solid #c8c8c8;background:var(--white);margin-top:14px}
.subscribe{display:block;margin:12px 0 0 186px;width:105px;height:30px;background:var(--button-dark);color:var(--white);font-size:13px;letter-spacing:.5px;text-align:center;line-height:30px}
.contact-list{margin-top:14px;font-size:13px;color:var(--ink-soft)}
.contact-list div{display:flex;align-items:baseline;margin-bottom:6px}
.contact-list .label{width:42px}
.contact-list .phone{font-size:18px;color:var(--ink)}
.footer-bottom{position:absolute;left:22px;right:22px;top:282px;border-top:1px solid var(--rule);display:flex;justify-content:space-between;padding:18px 50px 0 50px;font-size:11px;color:var(--ink)}
</style>
</head>
<body>

<section class="hero">
  <div class="hero-photo" role="img" aria-label="Photograph of a bright blue sky with soft white clouds"></div>
  <svg class="hero-arrow prev" width="36" height="52" viewBox="0 0 36 52" aria-hidden="true"><path d="M28 4 L8 26 L28 48" fill="none" stroke="#ffffff" stroke-width="8"/></svg>
  <svg class="hero-arrow next" width="36" height="52" viewBox="0 0 36 52" aria-hidden="true"><path d="M8 4 L28 26 L8 48" fill="none" stroke="#ffffff" stroke-width="6" opacity=".85"/></svg>
  <div class="hero-copy">
    <h1 class="hero-title condensed">Healthcare Strategic Consulting</h1>
    <p class="hero-text condensed">Lorem ipsum dolor sit amet, consectetuer adipiscing elit. Nam cursus. Morbi ut mi. Nullam enim leo, egestas id, condimentum at laoreet.</p>
    <span class="hero-button condensed">LEARN MORE ▸</span>
  </div>
</section>

<header class="site-header">
  <div class="brand">
    <div class="brand-name">The Varnholt Group</div>
    <div class="brand-tag">Healthcare Strategic Consulting</div>
  </div>
  <nav class="main-nav">
    <a href="#">Home</a><a href="#">About Us</a><a href="#">Services</a><a href="#">News &amp; Comments</a><a href="#">Contact Us</a>
  </nav>
</header>

<section class="welcome">
  <div class="welcome-main">
    <h2 class="section-title condensed">Welcome to The Varnholt Group</h2>
    <p class="welcome-lead">Morbi porta, libero id ullamcorper nonummy, nibh ligula pulvinar metus, eget consectetuer augue nisi quis lacus. Ut ac mi quis lacus mollis aliquam. Curabitur iaculis tempus eros.</p>
    <p class="welcome-body">Phasellus felis dolor, scelerisque a, tempus eget, lobortis id, libero. Donec scelerisque leo ac risus. Praesent sit amet est. In dictum, dolor eu dictum porttitor, enim felis viverra mi, eget luctus massa purus quis odio. Etiam nulla massa, pharetra facilisis, volutpat in, imperdiet sit amet, sem. Aliquam nec erat at purus cursus interdum. Vestibulum ligula augue, bibendum accumsan, vestibulum ut, commodo a, mi. Morbi ornare gravida elit. Integer congue, augue et malesuada iaculis, ipsum dui aliquet felis, at cursus magna nisl nec elit.</p>
    <span class="more-link condensed">Learn More ▸</span>
  </div>
  <div class="video-block">
    <h2 class="section-title condensed">Recent Video</h2>
    <div class="video-frame">
      <svg width="60" height="60" viewBox="0 0 60 60" aria-label="Play video" role="img"><circle cx="30" cy="30" r="26" fill="none" stroke="#fff" stroke-width="3"/><path d="M24 18 L42 30 L24 42 Z" fill="#fff"/></svg>
    </div>
  </div>
</section>

<section class="featured">
  <h2 class="section-title condensed">Featured Services</h2>
  <article class="service" style="left:57px">
    <div class="service-frame"><div class="service-photo" role="img" aria-label="Photograph of two business people shaking hands before a whiteboard of strategy notes" style="background:linear-gradient(135deg,#dfe4e1,#b9c2be 60%,#8c9693)"></div></div>
    <h3>Service Tittle Here</h3>
    <p>Lorem ipsum dolor sit amet, consectetuer adipiscing elit. Nam cursus. Morbi ut mi. Nullam enim leo, egestas id, condimentum at, laoreet mattis, massa.</p>
  </article>
  <article class="service" style="left:435px">
    <div class="service-frame"><div class="service-photo" role="img" aria-label="Photograph of yellow road direction signs across a blue landscape" style="background:linear-gradient(160deg,#5d6f9c,#3c4f7c 60%,#6a6a5a)"></div></div>
    <h3>Service Tittle Here</h3>
    <p>Lorem ipsum dolor sit amet, consectetuer adipiscing elit. Nam cursus. Morbi ut mi. Nullam enim leo, egestas id, condimentum at, laoreet mattis, massa.</p>
  </article>
  <article class="service" style="left:815px">
    <div class="service-frame"><div class="service-photo" role="img" aria-label="Photograph of two people arranging colourful sticky notes on a wall" style="background:linear-gradient(135deg,#efece4,#e3ddd0 60%,#c9c1b0)"></div></div>
    <h3>Service Tittle Here</h3>
    <p>Lorem ipsum dolor sit amet, consectetuer adipiscing elit. Nam cursus. Morbi ut mi. Nullam enim leo, egestas id, condimentum at, laoreet mattis, massa.</p>
  </article>
</section>

<section class="news">
  <h2 class="section-title condensed">Recent News</h2>
  <article class="news-item" style="left:54px;top:90px">
    <h4>Donec convallis pede venenatis nibh. Duis quam nam eget lacus.</h4>
    <p>Lorem ipsum dolor sit amet, consectetuer adipiscing elit. Nam cursus. Morbi ut mi. Nullam enim leo, egestas id, condimentum at, laoreet mattis, massa.</p>
    <span class="more-link condensed">Learn More ▸</span>
  </article>
  <article class="news-item" style="left:430px;top:90px">
    <h4>Ut velit enim, vestibulum non, fermentum nec, hendrerit quis, leo.</h4>
    <p>Lorem ipsum dolor sit amet, consectetuer adipiscing elit. Nam cursus. Morbi ut mi. Nullam enim leo, egestas id, condimentum at, laoreet mattis, massa.</p>
    <span class="more-link condensed">Learn More ▸</span>
  </article>
  <article class="news-item" style="left:803px;top:90px">
    <h4>Etiam est nunc, venenatis in, tristique eu, imperdiet ac, nisl.</h4>
    <p>Lorem ipsum dolor sit amet, consectetuer adipiscing elit. Nam cursus. Morbi ut mi. Nullam enim leo, egestas id, condimentum at, laoreet mattis, massa.</p>
    <span class="more-link condensed">Learn More</span>
  </article>
  <div class="news-divider"></div>
  <article class="news-item" style="left:51px;top:285px">
    <h4>Donec convallis pede venenatis nibh. Duis quam nam eget lacus.</h4>
    <p>Curabitur vel mi sit amet magna malesuada ultrices. Ut nisi erat, fermentum vel, congue id, euismod in, elit. Fusce ultricies, orci ac feugiat suscipit, leo massa sodales velit, et scelerisque mi tortor at ipsum. Proin orci odio, commodo ac.</p>
    <span class="more-link condensed">Learn More ▸</span>
  </article>
  <article class="news-item" style="left:430px;top:285px">
    <h4>Ut velit enim, vestibulum non, fermentum nec, hendrerit quis, leo.</h4>
    <p>Nunc tempus felis vitae urna. Vivamus porttitor, neque at volutpat rutrum, purus nisi eleifend libero, a tempus libero lectus feugiat felis. Morbi diam mauris, viverra in, gravida eu, mattis in, ante. Morbi eget arcu. Morbi porta, libero id ullamcorper nonummy, nibh ligula pulvinar metus</p>
    <span class="more-link condensed">Learn More ▸</span>
  </article>
  <article class="news-item" style="left:803px;top:285px">
    <h4>Class aptent taciti sociosqu ad litora torquent per conubia nostra</h4>
    <p>Lorem ipsum dolor sit amet, consectetuer adipiscing elit. Nam cursus. Morbi ut mi. Nullam enim leo, egestas id, condimentum at, laoreet mattis, massa.</p>
    <span class="more-link condensed">Learn More ▸</span>
  </article>
</section>

<footer class="site-footer">
  <div class="footer-col" style="left:115px;width:270px">
    <h5>Stay Connected</h5>
    <p>Please stay connect with us from anywhere from these followings.</p>
    <div class="social" aria-label="Social channels">
      <span role="img" aria-label="Social channel"></span><span role="img" aria-label="Social channel"></span><span role="img" aria-label="Social channel"></span><span role="img" aria-label="Social channel"></span><span role="img" aria-label="News feed"></span>
    </div>
  </div>
  <div class="footer-sep" style="left:408px"></div>
  <div class="footer-col" style="left:454px;width:300px">
    <h5>Newsletters Sign Up</h5>
    <p>Please sign up here for our latest newsletters.</p>
    <div class="newsletter-input"></div>
    <span class="subscribe">SUBSCRIBE</span>
  </div>
  <div class="footer-sep" style="left:775px"></div>
  <div class="footer-col" style="left:830px;width:300px">
    <h5>Contact Info</h5>
    <p>Your can contact us on these followings</p>
    <div class="contact-list">
      <div><span class="label">Tele:</span><span class="phone">(350) 555 0142</span></div>
      <div><span class="label">Fax:</span><span class="phone">(658) 555 0187</span></div>
      <div style="margin-top:10px"><span style="width:64px">Email us:</span><span>info@varnholtgroup.co.in</span></div>
    </div>
  </div>
  <div class="footer-bottom">
    <span>©2009-2012 The Varnholt Group. All Rights Reserved.</span>
    <span>Term of Use.&nbsp; Policy Privacy</span>
  </div>
</footer>

</body>
</html>
```